packaging Design Project

We would like to receive amazing design for our packaging sanitary napkin brand TORVELLE to catch customers
1)we have attached a file named CALDORA design but it is just a reference for taking the information please avoid to do a similar design as the brands are differents .As reference for the map of the design some modifications should be done on the sizes as per the following:
instead 12mm/24mm/90mm/24mm/12mm
it should be 25mm/35mm/120mm/35mm/25mm
instead 83mm/48mm/83mm/48mm/
it should be 105mm/65mm/105mm/65mm
2)our contact information have been changed and the new ones are as per the following:
Phone:(555)0-100-0147
:(555)0-100-0188
E-mail:info@harbeckwholesale.example
3)we have attached the TORVELLE sanitary pictures to be redesigned as per Brindle is done on its packaging.This is a very important point of the the design you will submit.
4)our company logo is attached
5)we need the design in CMYK format as it is for printing with the specified pantone number .
6)you can pick pictures from framequarry.example if you win we will buy it.
7)Please go to the supermarket or drugstore to have a better idea how the design should be but we are not required a copy of any brand.
8)five water drops in red or pink color should be in the both front to indicate the high absorption quality.
9) 8 pads.serviettes.toallas to indicate the qty per package.
10)a big word (MAXI) should be writted in the both front to indicate its high absorption.
11)275mm to indicate the lenght.
12)write SANITARY NAPKIN below the word TORVELLE.
13)reduce the size of our company logo and put it in the both front at the top on the left side.
14)please read the brief time to time because we are upgraded information time to time too.
15)Any doubt or question please send me a message.
N.B: the packaging design should be able to compete with BRINDLE PLUSH or Velumi so be creative to develop an amazing and innovative design.
Updates
please redesign the torvelle sanitary picture with each detail to be attractive,this is one of most importamt part of the design.
Reason: need more designs and some designers have required more time.
now the deadline is for may 13th.
please do not put barcode number.
Reason: need of amazing designs
don't work with the caldora sanitary picture but with the torvelle sanitary picture.you should design the torvelle sanitary picture to refelct all of its details to be amazing.
Reason: lack of good designs
Target Market(s)
woman from 12 to 45 years old
Industry/Entity Type
It Company
Requirements
Must have
- A)the design should have two fronts and the same information in the both front.
B) (MAXI) should be writted in the both front to indicate its high capacity of absorption.
C)five blood drops in red or pink color should be in the both front to indicate the high absorption quality.
D) 8 pads.serviettes.toallas to indicate the qty per package.
E)275mm to indicate the lenght
F)write SANITARY NAPKIN below the word
G)use fresh and innovative colors but feminine colors .
Nice to have
-reduce the size of our company logo and put it in the both front at the top of the left side.
Should not have
- -please don't put flowers because the pad dosen't have any scent or perfume.
-Please do not put barcode number.

```html
<!DOCTYPE html>
<html lang="en">
<head>
<meta charset="utf-8">
<title>Torvelle Maxi – carton dieline</title>
<link rel="stylesheet" href="https://fonts.googleapis.com/css2?family=Arimo:wght@400;700&family=Tenor+Sans&display=swap">
<style>
  :root{
    --plum:#7a1f4e;
    --plum-deep:#651840;
    --orchid:#a8507f;
    --white:#ffffff;
    --ink:#1f1a1d;
    --paper:#f3f1f2;
    --fold:#b9b3b6;
    --display:"Tenor Sans", sans-serif;
    --body:"Arimo", sans-serif;
  }
  *{box-sizing:border-box;margin:0;padding:0}
  html,body{width:1200px;height:900px;overflow:hidden;background:var(--paper)}
  .canvas{position:relative;width:1200px;height:900px}
  .dieline{position:absolute;left:300px;top:26px;width:449px;height:635px;transform:scale(1.336);transform-origin:0 0;font-family:var(--body);color:var(--white)}
  .row{position:absolute;left:0;width:449px;overflow:hidden;background:var(--plum)}
  .row--front-a{top:0;height:193px}
  .row--top{top:193px;height:132px;background:var(--plum-deep)}
  .row--front-b{top:325px;height:185px;transform:rotate(180deg)}
  .row--bottom{top:510px;height:125px;background:var(--plum-deep)}
  .row .waves{position:absolute;inset:0;width:100%;height:100%}
  .col{position:absolute;top:0;height:100%}
  .col--glue-l{left:0;width:48px}
  .col--side-l{left:48px;width:65px}
  .col--front{left:113px;width:225px}
  .col--side-r{left:338px;width:65px}
  .col--glue-r{left:403px;width:46px}
  .folds{position:absolute;inset:0;width:449px;height:635px;pointer-events:none}

  /* front face */
  .size-tag{position:absolute;width:38px;height:14px}
  .size-tag svg{position:absolute;inset:0}
  .size-tag span{position:absolute;inset:0;font:700 5px/14px var(--body);color:var(--white);text-align:center}
  .lockup{position:absolute;color:var(--ink)}
  .lockup .name{font:400 31px/1 var(--display);letter-spacing:-.5px}
  .lockup .maxi{font:400 19px/1 var(--display);color:var(--plum);letter-spacing:1.5px;text-align:right}
  .lockup .kind{font:700 5.6px/1.4 var(--body);color:var(--ink);text-align:right;letter-spacing:.2px}
  .front-lockup{left:38px;top:62px;width:150px}
  .drops{position:absolute;display:flex;gap:2px}
  .drops svg{width:6px;height:8px}
  .drops--row{left:14px;top:132px}
  .count-badge{position:absolute;width:52px;height:52px;border-radius:50%;background:var(--orchid);border:1.5px solid var(--white);display:flex;flex-direction:column;align-items:center;justify-content:center;text-align:center}
  .count-badge b{font:400 13px/1 var(--display)}
  .count-badge span{font:700 4.6px/1.25 var(--body);letter-spacing:.2px}
  .front-badge{left:162px;top:124px}

  /* side faces */
  .rotated{position:absolute;left:50%;top:50%}
  .side-lockup{transform:translate(-50%,-50%) rotate(90deg);width:96px}
  .side-lockup .name{font-size:22px}
  .side-lockup .maxi{font-size:13px;letter-spacing:1px}
  .side-lockup .kind{font-size:4.6px}
  .side-info{position:absolute;left:0;top:0;width:100%;height:100%}
  .side-info .drops--col{left:14px;top:56px;flex-direction:column;gap:3px}
  .side-info .size-tag{left:16px;top:70px;transform:rotate(90deg)}
  .side-info .count-badge{left:8px;top:122px;width:46px;height:46px;transform:rotate(90deg)}

  .contact{transform:translate(-50%,-50%) rotate(90deg);width:104px;color:var(--ink)}
  .contact .icons{display:flex;gap:8px;margin-bottom:5px}
  .contact .icon-slot{width:10px;height:10px;border:1.2px solid var(--ink);border-radius:50%}
  .contact .icon-slot.tri{border:none;width:0;height:0;border-left:6px solid transparent;border-right:6px solid transparent;border-bottom:10px solid var(--ink)}
  .contact p{font:400 4.2px/1.5 var(--body);white-space:nowrap}
  .contact .company{margin-top:4px;display:flex;align-items:center;gap:3px;font:700 6px/1 var(--body);color:var(--plum);letter-spacing:.4px}
  .contact .company i{width:6px;height:6px;border-radius:50%;background:var(--plum)}

  /* top panel */
  .copy{font:400 4.7px/1.45 var(--body);color:var(--white)}
  .copy + .copy{margin-top:5px}
  .top-copy{position:absolute;left:8px;right:8px;top:14px}
  .side-copy{transform:translate(-50%,-50%) rotate(90deg);width:96px;text-align:center}
  .side-copy--ccw{transform:translate(-50%,-50%) rotate(-90deg)}

  /* bottom panel */
  .steps{position:absolute;left:6px;top:12px;width:92px;list-style:none}
  .steps li{display:flex;gap:3px;margin-bottom:6px;font:400 4.4px/1.4 var(--body)}
  .steps li b{flex:none;width:7px;height:7px;border-radius:50%;background:var(--white);color:var(--plum);font:700 4.4px/7px var(--body);text-align:center}
  .pad-visual{position:absolute;left:118px;top:18px;width:62px;height:90px;border-radius:30px;background:linear-gradient(160deg,#ffffff,#dfe6f2);transform:rotate(-30deg)}
  .use-icons{position:absolute;left:14px;top:14px;display:flex;flex-direction:column;gap:14px}
  .use-icon{width:26px;height:26px;border-radius:3px;background:var(--white)}
  .use-note{position:absolute;left:52px;top:20px;transform:rotate(90deg);transform-origin:0 0;white-space:nowrap;font:400 4.4px/1 var(--body)}
</style>
</head>
<body>
<div class="canvas">
  <div class="dieline">

    <!-- FRONT A -->
    <section class="row row--front-a">
      <svg class="waves" viewBox="0 0 449 193" preserveAspectRatio="none" aria-hidden="true">
        <path fill="var(--orchid)" d="M0,23 C120,33 200,50 300,40 C360,34 410,26 449,26 L449,178 C380,168 330,158 260,166 C170,176 80,158 0,148 Z"/>
        <path fill="var(--white)" d="M0,31 C120,41 200,58 300,48 C360,42 410,34 449,34 L449,170 C380,160 330,150 260,158 C170,168 80,150 0,140 Z"/>
      </svg>
      <div class="col col--side-l">
        <div class="lockup rotated side-lockup">
          <div class="name">Torvelle</div>
          <div class="maxi">MAXI</div>
          <div class="kind">SANITARY NAPKIN</div>
        </div>
      </div>
      <div class="col col--front">
        <div class="size-tag" style="left:12px;top:36px">
          <svg viewBox="0 0 38 14"><path fill="var(--orchid)" d="M6,2 H32 Q36,2 36,7 Q36,12 32,12 H6 Q2,12 2,7 Q2,2 6,2Z M15,0 H23 V14 H15Z"/></svg>
          <span>275mm</span>
        </div>
        <div class="lockup front-lockup">
          <div class="name">Torvelle</div>
          <div class="maxi">MAXI</div>
          <div class="kind">SANITARY NAPKIN</div>
        </div>
        <div class="drops drops--row">
          <svg viewBox="0 0 6 8"><path fill="var(--plum)" d="M3,0 C4,3 6,4 6,5.5 A3,3 0 0 1 0,5.5 C0,4 2,3 3,0Z"/></svg>
          <svg viewBox="0 0 6 8"><path fill="var(--plum)" d="M3,0 C4,3 6,4 6,5.5 A3,3 0 0 1 0,5.5 C0,4 2,3 3,0Z"/></svg>
          <svg viewBox="0 0 6 8"><path fill="var(--plum)" d="M3,0 C4,3 6,4 6,5.5 A3,3 0 0 1 0,5.5 C0,4 2,3 3,0Z"/></svg>
          <svg viewBox="0 0 6 8"><path fill="var(--plum)" d="M3,0 C4,3 6,4 6,5.5 A3,3 0 0 1 0,5.5 C0,4 2,3 3,0Z"/></svg>
          <svg viewBox="0 0 6 8"><path fill="var(--plum)" d="M3,0 C4,3 6,4 6,5.5 A3,3 0 0 1 0,5.5 C0,4 2,3 3,0Z"/></svg>
        </div>
        <div class="count-badge front-badge"><b>8</b><span>PADS<br>SERVIETTES<br>TOALLAS</span></div>
      </div>
      <div class="col col--side-r">
        <div class="side-info">
          <div class="drops drops--col">
            <svg viewBox="0 0 6 8"><path fill="var(--plum)" d="M3,0 C4,3 6,4 6,5.5 A3,3 0 0 1 0,5.5 C0,4 2,3 3,0Z"/></svg>
            <svg viewBox="0 0 6 8"><path fill="var(--plum)" d="M3,0 C4,3 6,4 6,5.5 A3,3 0 0 1 0,5.5 C0,4 2,3 3,0Z"/></svg>
            <svg viewBox="0 0 6 8"><path fill="var(--plum)" d="M3,0 C4,3 6,4 6,5.5 A3,3 0 0 1 0,5.5 C0,4 2,3 3,0Z"/></svg>
            <svg viewBox="0 0 6 8"><path fill="var(--plum)" d="M3,0 C4,3 6,4 6,5.5 A3,3 0 0 1 0,5.5 C0,4 2,3 3,0Z"/></svg>
            <svg viewBox="0 0 6 8"><path fill="var(--plum)" d="M3,0 C4,3 6,4 6,5.5 A3,3 0 0 1 0,5.5 C0,4 2,3 3,0Z"/></svg>
          </div>
          <div class="size-tag">
            <svg viewBox="0 0 38 14"><path fill="var(--orchid)" d="M6,2 H32 Q36,2 36,7 Q36,12 32,12 H6 Q2,12 2,7 Q2,2 6,2Z M15,0 H23 V14 H15Z"/></svg>
            <span>275mm</span>
          </div>
          <div class="count-badge"><b>8</b><span>PADS<br>SERVIETTES<br>TOALLAS</span></div>
        </div>
      </div>
    </section>

    <!-- TOP PANEL -->
    <section class="row row--top">
      <div class="col col--side-l">
        <p class="copy rotated side-copy">Dispose of used pads wrapped in paper. Do not flush down the toilet.</p>
      </div>
      <div class="col col--front">
        <div class="top-copy">
          <p class="copy">Torvelle Maxi pads are made with a soft cotton-like top layer that keeps you dry and comfortable all day. The absorbent core locks in moisture quickly while the wings hold the pad firmly in place for extra security during active days.</p>
          <p class="copy">Les serviettes Torvelle Maxi offrent une protection longue durée. Las toallas Torvelle Maxi ofrecen protección segura y cómoda durante todo el día. Store in a cool, dry place.</p>
        </div>
      </div>
      <div class="col col--side-r">
        <p class="copy rotated side-copy side-copy--ccw">Change your pad every four to six hours for best comfort and hygiene.</p>
      </div>
    </section>

    <!-- FRONT B (printed upside down) -->
    <section class="row row--front-b">
      <svg class="waves" viewBox="0 0 449 185" preserveAspectRatio="none" aria-hidden="true">
        <path fill="var(--orchid)" d="M0,23 C120,33 200,50 300,40 C360,34 410,26 449,26 L449,170 C380,160 330,150 260,158 C170,168 80,150 0,140 Z"/>
        <path fill="var(--white)" d="M0,31 C120,41 200,58 300,48 C360,42 410,34 449,34 L449,162 C380,152 330,142 260,150 C170,160 80,142 0,132 Z"/>
      </svg>
      <div class="col col--side-l">
        <div class="lockup rotated side-lockup">
          <div class="name">Torvelle</div>
          <div class="maxi">MAXI</div>
          <div class="kind">SANITARY NAPKIN</div>
        </div>
      </div>
      <div class="col col--front">
        <div class="size-tag" style="left:12px;top:36px">
          <svg viewBox="0 0 38 14"><path fill="var(--orchid)" d="M6,2 H32 Q36,2 36,7 Q36,12 32,12 H6 Q2,12 2,7 Q2,2 6,2Z M15,0 H23 V14 H15Z"/></svg>
          <span>275mm</span>
        </div>
        <div class="lockup front-lockup">
          <div class="name">Torvelle</div>
          <div class="maxi">MAXI</div>
          <div class="kind">SANITARY NAPKIN</div>
        </div>
        <div class="drops drops--row" style="top:126px">
          <svg viewBox="0 0 6 8"><path fill="var(--plum)" d="M3,0 C4,3 6,4 6,5.5 A3,3 0 0 1 0,5.5 C0,4 2,3 3,0Z"/></svg>
          <svg viewBox="0 0 6 8"><path fill="var(--plum)" d="M3,0 C4,3 6,4 6,5.5 A3,3 0 0 1 0,5.5 C0,4 2,3 3,0Z"/></svg>
          <svg viewBox="0 0 6 8"><path fill="var(--plum)" d="M3,0 C4,3 6,4 6,5.5 A3,3 0 0 1 0,5.5 C0,4 2,3 3,0Z"/></svg>
          <svg viewBox="0 0 6 8"><path fill="var(--plum)" d="M3,0 C4,3 6,4 6,5.5 A3,3 0 0 1 0,5.5 C0,4 2,3 3,0Z"/></svg>
          <svg viewBox="0 0 6 8"><path fill="var(--plum)" d="M3,0 C4,3 6,4 6,5.5 A3,3 0 0 1 0,5.5 C0,4 2,3 3,0Z"/></svg>
        </div>
        <div class="count-badge front-badge" style="top:118px"><b>8</b><span>PADS<br>SERVIETTES<br>TOALLAS</span></div>
      </div>
      <div class="col col--side-r">
        <div class="rotated contact">
          <div class="icons"><i class="icon-slot"></i><i class="icon-slot tri"></i></div>
          <p>Phone:(555)0-100-0147 | :(555)0-100-0188</p>
          <p>E-mail: info@harbeckwholesale.example</p>
          <div class="company"><i></i>HARBECK</div>
        </div>
      </div>
    </section>

    <!-- BOTTOM PANEL -->
    <section class="row row--bottom">
      <div class="col col--side-l">
        <div class="use-icons">
          <div class="use-icon" role="img" aria-label="Icon: bin for disposal"></div>
          <div class="use-icon" role="img" aria-label="Icon: do not flush"></div>
        </div>
        <p class="use-note">Do not flush.</p>
      </div>
      <div class="col col--front">
        <ol class="steps">
          <li><b>1</b>Remove the pad from its wrapper and unfold it gently.</li>
          <li><b>2</b>Peel off the release paper from the back of the pad.</li>
          <li><b>3</b>Press the pad firmly into the centre of your underwear.</li>
          <li><b>4</b>Fold the wings around the edges and press to secure.</li>
        </ol>
        <div class="pad-visual" role="img" aria-label="Illustration of the winged Torvelle Maxi pad with numbered parts"></div>
      </div>
      <div class="col col--side-r">
        <div class="use-icons">
          <div class="use-icon" role="img" aria-label="Icon: wrap used pad"></div>
          <div class="use-icon" role="img" aria-label="Icon: fold the wings"></div>
        </div>
        <p class="use-note">Wrap and bin after use.</p>
      </div>
    </section>

    <svg class="folds" viewBox="0 0 449 635" aria-hidden="true">
      <g stroke="var(--fold)" stroke-width=".6" stroke-dasharray="3 2" fill="none">
        <line x1="16" y1="0" x2="16" y2="635"/>
        <line x1="48" y1="0" x2="48" y2="635"/>
        <line x1="113" y1="0" x2="113" y2="635"/>
        <line x1="338" y1="0" x2="338" y2="635"/>
        <line x1="403" y1="0" x2="403" y2="635"/>
        <line x1="433" y1="0" x2="433" y2="635"/>
        <line x1="0" y1="193" x2="449" y2="193"/>
        <line x1="0" y1="325" x2="449" y2="325"/>
        <line x1="0" y1="510" x2="449" y2="510"/>
      </g>
    </svg>
  </div>
</div>
</body>
</html>
```